Flag Order

We were just looking to order some branding flags to put on our rental equipment for our business. We would like different examples of the colors, shapes, sizes, backgrounds etc. Was thinking of just doing the plains icon instead of the whole logo on there. but open to ideas. preferably not a white background as they could get dirty,

```html
<!DOCTYPE html>
<html lang="en">
<head>
<meta charset="utf-8">
<title>Ridgeway Rentals – Banner Flags</title>
<link href="https://fonts.googleapis.com/css2?family=Figtree:wght@600;700&display=swap" rel="stylesheet">
<style>
  :root {
    --backdrop: #4d4d4d;
    --flag: #2b2b2b;
    --ink: #ffffff;
    --accent: #1e90e6;
  }
  * { margin: 0; padding: 0; box-sizing: border-box; }
  html, body {
    width: 1200px;
    height: 1200px;
    overflow: hidden;
    background: var(--backdrop);
  }
  .canvas {
    position: relative;
    width: 1200px;
    height: 1200px;
  }
  .flag {
    position: absolute;
    top: 254px;
    width: 186px;
    height: 518px;
    background: var(--flag);
    font-family: "Figtree", sans-serif;
    color: var(--ink);
  }
  .flag--left { left: 304px; }
  .flag--right { left: 748px; }
  .brand {
    position: absolute;
    top: 40px;
    left: 28px;
    display: flex;
    align-items: center;
    gap: 7px;
  }
  .brand__mark {
    width: 14px;
    height: 14px;
    background: var(--accent);
  }
  .brand__name {
    font-weight: 700;
    font-size: 15px;
    letter-spacing: 0.04em;
    text-transform: uppercase;
    color: var(--ink);
  }
  .tagline {
    position: absolute;
    top: 196px;
    left: 30px;
    font-weight: 600;
    font-size: 31px;
    line-height: 36px;
  }
  .accent-block {
    position: absolute;
    left: 132px;
    top: 412px;
    width: 44px;
    height: 66px;
    background: var(--accent);
  }
</style>
</head>
<body>
  <main class="canvas">
    <section class="flag flag--left">
      <div class="brand"><span class="brand__mark"></span><span class="brand__name">Ridgeway Rentals</span></div>
      <p class="tagline">Pushing<br>You<br>Further</p>
      <div class="accent-block"></div>
    </section>
    <section class="flag flag--right">
      <div class="brand"><span class="brand__mark"></span><span class="brand__name">Ridgeway Rentals</span></div>
      <p class="tagline">Pushing<br>You<br>Further</p>
      <div class="accent-block"></div>
    </section>
  </main>
</body>
</html>
```